Regional Valuation Adjustments - displaying differences in US regions by equipment category

We need a short flyer that illustrates how our business divides the country into regions, and for each region, how it differs from average across key equipment categories. Fairly straightforward, doesn't require a lot of fluff.

Target Market(s)

Construction companies and equipment owners

Industry/Entity Type

Construction

Font styles to use
Serif

Colors

Designer to choose colors to be used in the design.

Requirements
Must have
• - Header saying Brindle Sales - Regional Valuation Adjustments
• - Nice looking map (maybe half page?) showing the USA, divided into different colored regions (per the ppt document). Region breakpoints should pop a bit, maybe with negative space between them
• - Section for each region: Midwest, Northeast, Northwest, Southeast, Southwest, West)
• - Each section should show the 25 adjustment factors, organized by Category Group.
• - Show the adjustment factors as (1 - factor), so 102% shows as +2%, and 98% shows as -2%, with + or - sign included.
• - Show the factors as something more than just a number -- maybe a bar chart (above or below the 0 line, if its positive or negative)
• - Display the Global factor as "All Other" (do not use word "global"), and display it last.
Nice to have
• - Attached a sample flyer we have used in the past, could be used to guide look and feel

```html
<!DOCTYPE html>
<html lang="en">
<head>
<meta charset="utf-8">
<title>Brindle Sales – Regional Valuation Adjustments</title>
<link href="https://fonts.googleapis.com/css2?family=Arimo:ital,wght@0,400;0,700;1,700&family=Tinos&display=swap" rel="stylesheet">
<style>
  :root{
    --midwest:#9a7633;
    --northeast:#9d958a;
    --northwest:#c6b9a4;
    --southeast:#5b7489;
    --southwest:#8dadbe;
    --west:#a9a9a9;
    --panel:#e9eaeb;
    --band:#dcdcdc;
    --ink:#222222;
    --rule:#d6d6d6;
    --total:#dedede;
  }
  *{margin:0;padding:0;box-sizing:border-box}
  html,body{width:923px;height:1200px;overflow:hidden;background:#fff}
  .flyer{position:relative;width:923px;height:1200px;overflow:hidden;background:#fff;font-family:"Arimo",Arial,sans-serif}
  .header-shapes{position:absolute;left:0;top:0}
  .title{position:absolute;left:42px;top:50px;color:#fff;font-size:30px;font-weight:400;letter-spacing:.2px}
  .title em{font-weight:700;font-style:italic}
  .brand{position:absolute;left:690px;top:52px;display:flex;align-items:center;gap:8px;font-family:"Arimo",Arial,sans-serif;font-weight:700;font-size:27px;color:var(--ink)}
  .brand-mark{width:14px;height:14px;background:var(--midwest)}
  .map-panel{position:absolute;left:0;top:160px;width:923px;height:500px;background:var(--panel)}
  .map{position:absolute;left:72px;top:30px;width:778px;height:418px;border-radius:6px;
       background:linear-gradient(135deg,var(--northwest) 0%,var(--midwest) 40%,var(--northeast) 55%,var(--southeast) 75%,var(--southwest) 100%);opacity:.85}
  .legend{position:absolute;top:477px;left:215px;display:flex;gap:11px}
  .legend span{width:104px;height:25px;display:flex;align-items:center;justify-content:center;color:#fff;font-family:"Tinos",serif;font-size:17px}
  .divider{position:absolute;left:29px;top:677px;width:866px;height:1px;background:#c9c9c9}
  .adjustments{position:absolute;left:29px;top:688px;display:grid;grid-template-columns:176px repeat(6,104px);column-gap:11px}
  .adjustments .label{height:18.75px;font-family:"Tinos",serif;font-size:10px;color:var(--ink);display:flex;align-items:flex-end;padding-bottom:2px;border-bottom:1px solid var(--rule)}
  .adjustments .val{height:18.75px;display:flex;align-items:center;justify-content:center;color:#fff;font-size:13px}
  .mw{background:var(--midwest)} .ne{background:var(--northeast)} .nw{background:var(--northwest)}
  .se{background:var(--southeast)} .sw{background:var(--southwest)} .we{background:var(--west)}
  .adjustments .total{background:var(--total);color:#666;margin-top:4px}
  .adjustments .label.blank{border-bottom:none;margin-top:4px}
  .footer-shape{position:absolute;left:0;top:1152px}
  .contact{position:absolute;top:1162px;display:flex;align-items:center;gap:8px;color:#fff;font-weight:700;font-size:14px}
  .contact.phone{left:564px}
  .contact.email{left:716px}
</style>
</head>
<body>
<div class="flyer">
  <svg class="header-shapes" width="923" height="160" viewBox="0 0 923 160">
    <polygon points="588,22 660,160 0,160 0,136" fill="var(--band)"/>
    <polygon points="0,0 547,0 620,136 0,136" fill="var(--midwest)"/>
  </svg>
  <h1 class="title">Regional <em>Valuation Adjustments</em></h1>
  <div class="brand"><span>Brindle Sales</span><span class="brand-mark"></span></div>

  <section class="map-panel">
    <div class="map" role="img" aria-label="Map of the contiguous United States divided into six coloured valuation regions: Northwest, West, Midwest, Southwest, Southeast and Northeast"></div>
    <div class="legend">
      <span class="mw">Midwest</span><span class="ne">Northeast</span><span class="nw">Northwest</span>
      <span class="se">Southeast</span><span class="sw">Southwest</span><span class="we">West</span>
    </div>
  </section>

  <div class="divider"></div>

  <div class="adjustments">
    <div class="label">Articulating Booms</div><div class="val mw">+1</div><div class="val ne">-1</div><div class="val nw">+4</div><div class="val se">+2</div><div class="val sw">-6</div><div class="val we">+2</div>
    <div class="label">Scissor Lifts</div><div class="val mw">-1</div><div class="val ne">-6</div><div class="val nw">+3</div><div class="val se">-3</div><div class="val sw">0</div><div class="val we">+3</div>
    <div class="label">Telescopic Booms</div><div class="val mw">-4</div><div class="val ne">-1</div><div class="val nw">+1</div><div class="val se">-1</div><div class="val sw">0</div><div class="val we">+2</div>
    <div class="label">Towable Booms</div><div class="val mw">-4</div><div class="val ne">-1</div><div class="val nw">+1</div><div class="val se">-1</div><div class="val sw">0</div><div class="val we">+2</div>
    <div class="label">Articulated Trucks</div><div class="val mw">+2</div><div class="val ne">0</div><div class="val nw">+7</div><div class="val se">-2</div><div class="val sw">-3</div><div class="val we">+4</div>
    <div class="label">Backhoe Loaders</div><div class="val mw">-1</div><div class="val ne">-2</div><div class="val nw">+5</div><div class="val se">-2</div><div class="val sw">-1</div><div class="val we">+2</div>
    <div class="label">Crawler Loaders</div><div class="val mw">+4</div><div class="val ne">+3</div><div class="val nw">+3</div><div class="val se">-2</div><div class="val sw">-3</div><div class="val we">+7</div>
    <div class="label">Dozers</div><div class="val mw">+4</div><div class="val ne">+3</div><div class="val nw">+3</div><div class="val se">-2</div><div class="val sw">-3</div><div class="val we">+7</div>
    <div class="label">Excavators</div><div class="val mw">+2</div><div class="val ne">0</div><div class="val nw">+7</div><div class="val se">-2</div><div class="val sw">-3</div><div class="val we">+4</div>
    <div class="label">Motors Graders</div><div class="val mw">+2</div><div class="val ne">0</div><div class="val nw">+7</div><div class="val se">-2</div><div class="val sw">-3</div><div class="val we">+4</div>
    <div class="label">Rigid Trucks</div><div class="val mw">+2</div><div class="val ne">0</div><div class="val nw">+7</div><div class="val se">-2</div><div class="val sw">-3</div><div class="val we">+4</div>
    <div class="label">Scrapers</div><div class="val mw">+2</div><div class="val ne">0</div><div class="val nw">+7</div><div class="val se">-2</div><div class="val sw">-3</div><div class="val we">+4</div>
    <div class="label">Skid Steers Loaders</div><div class="val mw">0</div><div class="val ne">+1</div><div class="val nw">+7</div><div class="val se">-4</div><div class="val sw">-3</div><div class="val we">+2</div>
    <div class="label">Track Loaders</div><div class="val mw">+1</div><div class="val ne">-1</div><div class="val nw">+5</div><div class="val se">-2</div><div class="val sw">-3</div><div class="val we">+5</div>
    <div class="label">Wheel Dozers</div><div class="val mw">0</div><div class="val ne">+2</div><div class="val nw">+7</div><div class="val se">-5</div><div class="val sw">-3</div><div class="val we">+4</div>
    <div class="label">Wheel Excavators</div><div class="val mw">+2</div><div class="val ne">0</div><div class="val nw">+7</div><div class="val se">-2</div><div class="val sw">-3</div><div class="val we">+4</div>
    <div class="label">Wheel Loaders</div><div class="val mw">0</div><div class="val ne">+2</div><div class="val nw">+7</div><div class="val se">-5</div><div class="val sw">-3</div><div class="val we">+4</div>
    <div class="label">Forklif Trucks</div><div class="val mw">-3</div><div class="val ne">-1</div><div class="val nw">0</div><div class="val se">-1</div><div class="val sw">+3</div><div class="val we">-2</div>
    <div class="label">Mast Lifts</div><div class="val mw">-1</div><div class="val ne">+6</div><div class="val nw">+3</div><div class="val se">-3</div><div class="val sw">0</div><div class="val we">+3</div>
    <div class="label">Rough- Terrain Forklifts</div><div class="val mw">-3</div><div class="val ne">-1</div><div class="val nw">+3</div><div class="val se">-2</div><div class="val sw">-4</div><div class="val we">+7</div>
    <div class="label">Telehandlers</div><div class="val mw">-3</div><div class="val ne">-1</div><div class="val nw">+3</div><div class="val se">-2</div><div class="val sw">-4</div><div class="val we">+7</div>
    <div class="label">Lighting Equipment</div><div class="val mw">-4</div><div class="val ne">-1</div><div class="val nw">-5</div><div class="val se">+2</div><div class="val sw">-2</div><div class="val we">+7</div>
    <div class="label">Pickup Trucks</div><div class="val mw">-5</div><div class="val ne">-8</div><div class="val nw">+5</div><div class="val se">+3</div><div class="val sw">-5</div><div class="val we">+4</div>
    <div class="label blank"></div><div class="val total">-2</div><div class="val total">-2</div><div class="val total">+2</div><div class="val total">-1</div><div class="val total">-2</div><div class="val total">+2</div>
  </div>

  <svg class="footer-shape" width="923" height="48" viewBox="0 0 923 48">
    <polygon points="477,48 528,0 923,0 923,48" fill="#231f20"/>
  </svg>
  <div class="contact phone">
    <svg width="22" height="22" viewBox="0 0 24 24" fill="none" stroke="#fff" stroke-width="1.6" stroke-linejoin="round"><path d="M5 3h4l2 5-3 2a12 12 0 0 0 6 6l2-3 5 2v4a2 2 0 0 1-2 2A17 17 0 0 1 3 5a2 2 0 0 1 2-2z"/></svg>
    <span>555 010 4420</span>
  </div>
  <div class="contact email">
    <svg width="24" height="18" viewBox="0 0 24 18" fill="none" stroke="#fff" stroke-width="1.6"><rect x="1" y="1" width="22" height="16"/><path d="M1 1l11 9 11-9M1 17l8-7M23 17l-8-7"/></svg>
    <span>info@brindlesales.com</span>
  </div>
</div>
</body>
</html>
```